KVT New York

i need a marketing piece for my upcoming live dental hands on course. highlighting that it is in new york, with photo of new york city or sky line

```html
<!DOCTYPE html>
<html lang="en">
<head>
<meta charset="utf-8">
<title>KVT New York – Hands-On Course</title>
<link rel="stylesheet" href="https://fonts.googleapis.com/css2?family=Poppins:ital,wght@0,400;0,700;0,800;1,700&family=Montserrat:wght@400;500&display=swap">
<style>
  :root {
    --sky-top: #2fa8dc;
    --sky-mid: #8fc7e6;
    --city-low: #6d7f93;
    --blue-light: #1eaee6;
    --blue-mid: #2076ad;
    --navy: #233a72;
    --gold: #f2cf6c;
    --white: #ffffff;
    --frame: #e6e6e6;
    --button: #e8e8ea;
    --ink: #2f2f33;
    --bullet: #e3eef8;
    --photo-warm: #e4b9a5;
    --photo-light: #efd3c5;
  }
  * { margin: 0; padding: 0; box-sizing: border-box; }
  html, body { width: 848px; height: 1200px; overflow: hidden; background: #dfe3e8; }
  .poster {
    position: relative;
    width: 848px;
    height: 1200px;
    overflow: hidden;
    background: linear-gradient(100deg, var(--blue-light) 0%, var(--blue-mid) 45%, var(--navy) 100%);
    font-family: "Poppins", sans-serif;
    color: var(--white);
  }
  .skyline-photo {
    position: absolute;
    left: 0; top: 0;
    width: 848px; height: 429px;
    background: linear-gradient(180deg, var(--sky-top) 0%, var(--sky-mid) 45%, #9fb3c4 70%, var(--city-low) 100%);
  }
  .frame {
    position: absolute;
    left: 36px; top: 36px;
    width: 777px; height: 1115px;
    border: 4px solid var(--frame);
  }
  .brand-tab {
    position: absolute;
    left: 207px; top: 56px;
    width: 434px; height: 89px;
    background: var(--white);
    border-radius: 34px 44px 0 34px;
    display: flex;
    align-items: center;
    padding-left: 22px;
    gap: 14px;
  }
  .brand-name {
    font-weight: 800;
    font-size: 58px;
    line-height: 1;
    color: var(--navy);
    letter-spacing: 1px;
  }
  .brand-dot {
    width: 12px; height: 12px;
    background: var(--blue-light);
  }
  .brand-descriptor {
    font-family: "Montserrat", sans-serif;
    font-weight: 500;
    font-size: 21px;
    line-height: 1.15;
    color: #111;
  }
  .smile-photo {
    position: absolute;
    left: 139px; top: 316px;
    width: 571px; height: 259px;
    border: 9px solid var(--white);
    background: linear-gradient(110deg, var(--photo-warm) 0%, var(--photo-light) 50%, var(--photo-warm) 100%);
  }
  .headline {
    position: absolute;
    left: 0; top: 615px;
    width: 848px;
    text-align: center;
    font-weight: 700;
    text-transform: uppercase;
  }
  .headline-title {
    color: var(--gold);
    font-size: 60px;
    line-height: 70px;
  }
  .headline-course {
    color: var(--white);
    font-size: 67px;
    font-weight: 700;
    line-height: 76px;
  }
  .details {
    position: absolute;
    left: 0; top: 850px;
    width: 848px;
    font-family: "Montserrat", sans-serif;
    font-size: 21px;
  }
  .detail {
    display: flex;
    justify-content: center;
    align-items: center;
    gap: 14px;
    height: 36px;
  }
  .detail svg { flex: none; }
  .register-line {
    position: absolute;
    left: 92px; top: 951px;
    display: flex;
    align-items: center;
    gap: 4px;
    font-style: italic;
    font-weight: 700;
    font-size: 26px;
  }
  .register-url {
    background: var(--white);
    color: var(--navy);
    border-radius: 8px;
    padding: 0 9px 0 5px;
    line-height: 36px;
  }
  .benefits {
    position: absolute;
    left: 92px; top: 1003px;
    list-style: none;
    font-size: 16.2px;
    font-weight: 400;
    color: var(--bullet);
    letter-spacing: 0.2px;
  }
  .benefits li {
    display: flex;
    align-items: center;
    gap: 12px;
    height: 34px;
  }
  .register-button {
    position: absolute;
    left: 304px; top: 1126px;
    width: 241px; height: 45px;
    background: var(--button);
    border-radius: 22px;
    color: var(--ink);
    font-weight: 700;
    font-size: 20px;
    display: flex;
    align-items: center;
    justify-content: center;
  }
</style>
</head>
<body>
<main class="poster">
  <div class="skyline-photo" role="img" aria-label="New York City skyline with a suspension bridge over the river under a blue sky"></div>
  <div class="frame"></div>

  <header class="brand-tab">
    <span class="brand-name">KVT</span>
    <span class="brand-dot"></span>
    <span class="brand-descriptor">Kinetic Vector<br>Treatment</span>
  </header>

  <div class="smile-photo" role="img" aria-label="Close-up photo of a smile with orthodontic braces"></div>

  <h1 class="headline">
    <span class="headline-title">Kinetic Vector<br>Treatment</span><br>
    <span class="headline-course">Hands-On Course</span>
  </h1>

  <section class="details">
    <p class="detail">
      <svg width="28" height="26" viewBox="0 0 28 26" aria-hidden="true">
        <rect x="1" y="3" width="26" height="22" rx="3" fill="#fff"/>
        <rect x="6" y="0" width="3" height="6" rx="1" fill="#fff"/>
        <rect x="19" y="0" width="3" height="6" rx="1" fill="#fff"/>
        <g fill="#2a7fb6">
          <rect x="5" y="11" width="4" height="3"/><rect x="12" y="11" width="4" height="3"/><rect x="19" y="11" width="4" height="3"/>
          <rect x="5" y="17" width="4" height="3"/><rect x="12" y="17" width="4" height="3"/><rect x="19" y="17" width="4" height="3"/>
        </g>
      </svg>
      <span>November 12-13th, 2026</span>
    </p>
    <p class="detail">
      <svg width="22" height="28" viewBox="0 0 22 28" aria-hidden="true">
        <path d="M11 0C5 0 0 4.8 0 10.7 0 18 11 28 11 28s11-10 11-17.3C22 4.8 17 0 11 0z" fill="#fff"/>
        <circle cx="11" cy="10.5" r="4" fill="#2874ab"/>
      </svg>
      <span>&nbsp;New York, USA</span>
    </p>
  </section>

  <p class="register-line">Register today at <span class="register-url">brightarchdental.com</span></p>

  <ul class="benefits">
    <li><svg width="24" height="24" viewBox="0 0 24 24" aria-hidden="true"><path d="M21 10.5A10 10 0 1 1 15.5 3" fill="none" stroke="#fff" stroke-width="1.6" stroke-linecap="round"/><path d="M7.5 11.5l4 4L22 4" fill="none" stroke="#fff" stroke-width="1.8" stroke-linecap="round" stroke-linejoin="round"/></svg>Understand how teeth move and how to move them</li>
    <li><svg width="24" height="24" viewBox="0 0 24 24" aria-hidden="true"><path d="M21 10.5A10 10 0 1 1 15.5 3" fill="none" stroke="#fff" stroke-width="1.6" stroke-linecap="round"/><path d="M7.5 11.5l4 4L22 4" fill="none" stroke="#fff" stroke-width="1.8" stroke-linecap="round" stroke-linejoin="round"/></svg>Improve the success rates of your ClearTrack cases</li>
    <li><svg width="24" height="24" viewBox="0 0 24 24" aria-hidden="true"><path d="M21 10.5A10 10 0 1 1 15.5 3" fill="none" stroke="#fff" stroke-width="1.6" stroke-linecap="round"/><path d="M7.5 11.5l4 4L22 4" fill="none" stroke="#fff" stroke-width="1.8" stroke-linecap="round" stroke-linejoin="round"/></svg>Orthodontics is the key to better Implant, Veneer and FMR outcomes</li>
  </ul>

  <div class="register-button">Register Today</div>
</main>
</body>
</html>
```